Update Theme for existing site

Update Theme and allow for integration of product update sheets
Updates

Please use the existing website veltrunaxis.com for content. Would like a new homepage and ability to update products, ideally by placing PDF files in a set directory location. The current theme is an old wordpress, but we have had problems updating it. A similar company to ours would be: brimtel-works.com Quorvane.io to get an idea of what we would like.

Coding

```html
<!DOCTYPE html>
<html lang="en">
<head>
<meta charset="utf-8">
<title>Veltrun Axis — A Driving Force in Satellites</title>
<link rel="stylesheet" href="https://fonts.googleapis.com/css2?family=Montserrat:wght@400;500;700;800&family=Old+Standard+TT:wght@400;700&family=Hind:wght@400;500&display=swap">
<style>
  :root {
    --space-black: #05060c;
    --space-navy: #0d0f38;
    --brand-blue: #1c27b2;
    --white: #ffffff;
    --ink: #1b1b1f;
    --muted: #7a7a80;
    --link-blue: #1c27b2;
    --serif: "Old Standard TT", Georgia, serif;
    --sans: "Montserrat", Arial, sans-serif;
    --body: "Hind", Arial, sans-serif;
  }
  * { box-sizing: border-box; margin: 0; padding: 0; }
  html, body { width: 1200px; height: 2817px; overflow: hidden; }
  body { position: relative; background: var(--space-black); color: var(--white); font-family: var(--body); }

  /* Hero */
  .hero { position: absolute; left: 0; top: 0; width: 1200px; height: 781px; overflow: hidden;
    background: radial-gradient(ellipse 900px 700px at 0% 0%, #7c9ac4 0%, #2c4a7e 35%, #0a1020 62%, #030409 80%); }
  .hero-visual { position: absolute; left: 300px; top: 230px; width: 840px; height: 420px;
    background: radial-gradient(ellipse at center, rgba(160,165,175,.45), rgba(60,65,75,.15) 55%, transparent 72%); }
  .site-header { position: absolute; left: 0; top: 0; width: 1200px; height: 120px; }
  .brand { position: absolute; left: 90px; top: 38px; font-family: var(--serif); font-size: 34px; color: var(--white); }
  .main-nav { position: absolute; right: 90px; top: 48px; display: flex; gap: 0; }
  .main-nav a { color: var(--white); text-decoration: none; font-family: var(--sans); font-size: 15px; margin-left: 41px; }
  .hero-title { position: absolute; left: 88px; top: 246px; font-family: var(--sans); font-weight: 700;
    font-size: 68px; line-height: 70px; letter-spacing: .5px; }
  .scroll-down { position: absolute; left: 570px; top: 652px; }

  /* Intro band */
  .intro { position: absolute; left: 0; top: 781px; width: 1200px; height: 196px; background: var(--brand-blue);
    display: flex; align-items: center; justify-content: center; text-align: center; }
  .intro p { font-family: var(--serif); font-size: 25px; line-height: 36px; max-width: 900px; }

  /* Services */
  .services { position: absolute; left: 0; top: 977px; width: 1200px; height: 826px;
    background: radial-gradient(ellipse at 60% 40%, #0e1020 0%, var(--space-black) 70%); }
  .section-title { position: absolute; left: 0; width: 1200px; text-align: center; font-family: var(--serif);
    font-weight: 400; font-size: 48px; letter-spacing: 1px; }
  .services .section-title { top: 88px; }
  .service-card { position: absolute; width: 291px; height: 306px; background: var(--white); border-radius: 12px;
    text-align: center; padding: 30px 18px 0; color: var(--ink); }
  .service-card h3 { font-family: var(--sans); font-weight: 500; font-size: 25px; line-height: 30px; margin-bottom: 14px; }
  .service-card p { font-family: var(--body); font-size: 17px; line-height: 28px; color: var(--muted); }
  .service-card .more { display: block; margin-top: 14px; font-family: var(--serif); font-weight: 700; font-size: 14px;
    letter-spacing: .5px; color: var(--link-blue); text-decoration: none; }
  .card-mech { left: 90px; top: 154px; z-index: 1; }
  .card-elec { left: 381px; top: 238px; z-index: 2; }
  .card-system { left: 135px; top: 385px; z-index: 3; background: var(--brand-blue); color: var(--white); }
  .card-system p { color: var(--white); }
  .card-system .more { color: var(--white); }
  .service-visual { position: absolute; left: 780px; top: 272px; width: 385px; height: 330px;
    background: radial-gradient(ellipse at 45% 50%, #c9ccd2 0%, #c46a2a 30%, rgba(80,60,50,.4) 55%, transparent 72%); }

  /* Products */
  .products { position: absolute; left: 0; top: 1803px; width: 1200px; height: 635px;
    background: radial-gradient(ellipse at 50% 50%, #1a1e5a 0%, var(--space-navy) 65%); }
  .products .section-title { top: 94px; }
  .product-card { position: absolute; top: 178px; width: 323px; height: 333px; }
  .product-image { width: 323px; height: 244px; }
  .product-label { height: 89px; background: var(--white); text-align: center; padding-top: 18px; color: var(--ink); }
  .product-label h3 { font-family: var(--sans); font-weight: 500; font-size: 21px; }
  .product-label a { font-family: var(--body); font-style: italic; font-size: 13px; color: var(--link-blue); text-decoration: none; }
  .prod-propulsion { left: 90px; } .prod-propulsion .product-image { background: linear-gradient(160deg, #2a2a2a, #a8a8a8 50%, #111); }
  .prod-power { left: 438px; } .prod-power .product-image { background: radial-gradient(ellipse 60% 25% at 50% 50%, #d8c020, #2a2b35 80%); }
  .prod-modules { left: 787px; } .prod-modules .product-image { background: linear-gradient(160deg, #151515, #8a7a3a 45%, #b89a20 70%, #222); }
  .carousel-arrow { position: absolute; top: 330px; }
  .arrow-prev { left: 36px; } .arrow-next { left: 1148px; }

  /* Footer */
  .site-footer { position: absolute; left: 0; top: 2438px; width: 1200px; height: 379px; background: var(--space-black);
    text-align: center; }
  .footer-brand { position: absolute; left: 0; top: 100px; width: 1200px; font-family: var(--serif); font-size: 44px; }
  .social { position: absolute; left: 482px; top: 204px; display: flex; gap: 11px; }
  .social span { width: 50px; height: 50px; border: 2px solid var(--white); border-radius: 50%; display: block; }
  .footer-nav { position: absolute; left: 0; top: 278px; width: 1200px; font-family: var(--sans); font-size: 14px; }
  .footer-nav a { color: var(--white); text-decoration: none; }
  .footer-nav .sep { margin: 0 14px; }
  .copyright { position: absolute; left: 0; top: 311px; width: 1200px; font-family: var(--sans); font-size: 12px; }
</style>
</head>
<body>
  <section class="hero">
    <div class="hero-visual" role="img" aria-label="Space station orbiting above the curve of the Earth"></div>
    <header class="site-header">
      <div class="brand">Veltrun Axis</div>
      <nav class="main-nav">
        <a href="#">Home</a><a href="#">Products</a><a href="#">Services</a><a href="#">Awards</a><a href="#">News</a><a href="#">About</a><a href="#">Contact</a>
      </nav>
    </header>
    <h1 class="hero-title">A DRIVING FORCE<br>IN SATELLITES</h1>
    <svg class="scroll-down" width="60" height="60" viewBox="0 0 60 60" aria-label="Scroll down">
      <circle cx="30" cy="30" r="27" fill="none" stroke="#fff" stroke-width="3"/>
      <polyline points="18,22 30,33 42,22" fill="none" stroke="#fff" stroke-width="3.5" stroke-linecap="round" stroke-linejoin="round"/>
      <polyline points="18,32 30,43 42,32" fill="none" stroke="#fff" stroke-width="3.5" stroke-linecap="round" stroke-linejoin="round"/>
    </svg>
  </section>

  <section class="intro">
    <p>Veltrun Axis designs and builds high-capability power and propulsion components, subsystems, and fully-integrated buses for CubeSats and small satellites.</p>
  </section>

  <section class="services">
    <h2 class="section-title">OUR SERVICES</h2>
    <article class="service-card card-mech">
      <h3>Mechanical<br>Engineering</h3>
      <p>Veltrun Axis's engineers possess a broad array of skills and experience, on spacecraft as small as CubeSats, to larger communications satellites...</p>
    </article>
    <article class="service-card card-elec">
      <h3>Electrical<br>Engineering</h3>
      <p>Veltrun Axis's engineers possess a broad array of skills and experience, on spacecraft as small as CubeSats, to larger communications satellites...</p>
      <a class="more" href="#">READ MORE</a>
    </article>
    <article class="service-card card-system">
      <h3>System<br>Design</h3>
      <p>Veltrun Axis's engineers possess a broad array of skills and experience, on spacecraft as small as CubeSats, to larger communications satellites...</p>
      <a class="more" href="#">READ MORE</a>
    </article>
    <div class="service-visual" role="img" aria-label="Space shuttle with orange fuel tank and boosters"></div>
  </section>

  <section class="products">
    <h2 class="section-title">FEATURE PRODUCTS</h2>
    <svg class="carousel-arrow arrow-prev" width="20" height="30" viewBox="0 0 20 30" aria-label="Previous"><polyline points="14,5 5,15 14,25" fill="none" stroke="#fff" stroke-width="4"/></svg>
    <article class="product-card prod-propulsion">
      <div class="product-image" role="img" aria-label="Metal propulsion thruster unit"></div>
      <div class="product-label"><h3>Propulsion Products</h3><a href="#">View Details</a></div>
    </article>
    <article class="product-card prod-power">
      <div class="product-image" role="img" aria-label="Yellow flexible solar array panel"></div>
      <div class="product-label"><h3>Power Products</h3><a href="#">View Details</a></div>
    </article>
    <article class="product-card prod-modules">
      <div class="product-image" role="img" aria-label="Assembled spacecraft module components"></div>
      <div class="product-label"><h3>Spacecraft Modules</h3><a href="#">View Details</a></div>
    </article>
    <svg class="carousel-arrow arrow-next" width="20" height="30" viewBox="0 0 20 30" aria-label="Next"><polyline points="6,5 15,15 6,25" fill="none" stroke="#fff" stroke-width="4"/></svg>
  </section>

  <footer class="site-footer">
    <div class="footer-brand">Veltrun Axis</div>
    <div class="social" aria-label="Social links"><span></span><span></span><span></span><span></span></div>
    <nav class="footer-nav">
      <a href="#">Home</a><span class="sep">I</span><a href="#">Products</a><span class="sep">I</span><a href="#">Services</a><span class="sep">I</span><a href="#">Awards</a><span class="sep">I</span><a href="#">News</a><span class="sep">I</span><a href="#">About</a><span class="sep">I</span><a href="#">Contact</a>
    </nav>
    <p class="copyright">Copyrights © 2019,The Company Name. All rights reserved.</p>
  </footer>
</body>
</html>
```